NEW Inspirational Young Adults Book Needs Cover Design

The title of the book is:
The Lantern and the Kite: Notes on Money, Friends, Cities, Music, and Courage in Early Life
This a short book and I imagine A5 in size. Needs to be funky and appealing for the 15-25 age group. I have always imagined it some how featuring a frog and a fish. I have attached the contents and a page of the intro to show how the frog and fish fit with the book.

Target Market(s)

Young adults 15-25 years age

Industry/Entity Type

Education

Font styles to use
Sans Serif

Requirements
Must have
• a frog and a fish

```html
<!DOCTYPE html>
<html lang="en">
<head>
<meta charset="utf-8">
<title>The Lantern and the Kite — Book Cover</title>
<link rel="stylesheet" href="https://fonts.googleapis.com/css2?family=Luckiest+Guy&family=Titan+One&family=Fredoka:wght@700&family=Crimson+Text:wght@400&display=block">
<style>
  :root {
    --paper-light: #fcca4a;
    --paper-mid: #f8b531;
    --paper-deep: #f19f1f;
    --ink: #111111;
    --accent-red: #b5161b;
    --fish-top: #8d4f58;
    --fish-mid: #b08a8c;
    --fish-belly: #c9c3b8;
    --frog-green: #3f7a6a;
    --frog-dark: #2c5a4d;
    --frog-orange: #e0782a;
  }
  * { margin: 0; padding: 0; box-sizing: border-box; }
  html, body { width: 845px; height: 1200px; overflow: hidden; }
  .cover {
    position: relative;
    width: 845px;
    height: 1200px;
    overflow: hidden;
    background:
      radial-gradient(ellipse 70% 18% at 40% 30%, rgba(255,220,120,0.55), transparent 70%),
      radial-gradient(ellipse 80% 14% at 60% 55%, rgba(255,215,110,0.45), transparent 70%),
      radial-gradient(ellipse 60% 20% at 30% 85%, rgba(240,150,20,0.35), transparent 70%),
      linear-gradient(175deg, var(--paper-deep) 0%, var(--paper-mid) 25%, var(--paper-light) 50%, var(--paper-mid) 75%, var(--paper-deep) 100%);
  }
  .title {
    position: absolute;
    top: 78px;
    left: 0;
    width: 100%;
    text-align: center;
    font-family: "Luckiest Guy", "Titan One", sans-serif;
    font-weight: 400;
    text-transform: uppercase;
    color: var(--ink);
    line-height: 1;
  }
  .title-line { display: block; }
  .title-line--first { font-size: 108px; letter-spacing: 1px; }
  .title-joiner { display: block; font-size: 30px; margin: 0 0 4px; }
  .title-line--second { font-size: 138px; letter-spacing: 2px; }
  .subtitle {
    position: absolute;
    top: 432px;
    left: 0;
    width: 100%;
    text-align: center;
    font-family: "Fredoka", sans-serif;
    font-weight: 700;
    font-variant: small-caps;
    font-size: 40px;
    line-height: 56px;
    color: var(--ink);
  }
  .subtitle .highlight { color: var(--accent-red); }
  .art-fish {
    position: absolute;
    left: -20px;
    top: 668px;
    width: 362px;
    height: 330px;
    border-radius: 45% 55% 50% 40% / 50% 50% 50% 50%;
    background: linear-gradient(180deg, var(--fish-top) 0%, var(--fish-mid) 50%, var(--fish-belly) 100%);
  }
  .art-frog {
    position: absolute;
    left: 596px;
    top: 628px;
    width: 260px;
    height: 452px;
    border-radius: 45% 0 0 45% / 35% 0 0 35%;
    background: radial-gradient(ellipse 60% 30% at 55% 50%, var(--frog-green) 0%, var(--frog-dark) 60%, var(--frog-orange) 100%);
  }
  .author {
    position: absolute;
    top: 1090px;
    left: 0;
    width: 100%;
    text-align: center;
    font-family: "Crimson Text", serif;
    font-size: 42px;
    color: var(--ink);
  }
  .author-by { font-size: 28px; }
</style>
</head>
<body>
  <main class="cover">
    <h1 class="title">
      <span class="title-line title-line--first">The Lantern</span>
      <span class="title-joiner">and</span>
      <span class="title-line title-line--second">The Kite</span>
    </h1>
    <p class="subtitle">
      Notes on Money, <span class="highlight">Friends</span>, Cities,<br>
      <span class="highlight">Music</span>, and Courage<br>
      in <span class="highlight">Early Life</span>
    </p>
    <div class="art-fish" role="img" aria-label="Illustration of a red mullet fish facing right"></div>
    <div class="art-frog" role="img" aria-label="Illustration of a green tree frog seen from above, facing left"></div>
    <p class="author"><span class="author-by">By</span> Dana Whitlock</p>
  </main>
</body>
</html>
```